Waterjet manufacturing company needs brochure design

We need a brochure that outlines why waterjet manufacturing is beneficial for a variety of industries, our capabilities, core competencies and competitive advantages (see attached documents). The design should include our logo and include the same colours. (Dark blue RGB – 2,86,162, Light Blue RGB – 0,146,201). The design should be very clean, professional and eye catching. I've attached a few photos that can be used. Regarding the photo of the robot, please make the background white.

Manufacturing, construction, aerospace, home building

• - exact Logo colours included in design (see description)
• - booklet style design (not tri-fold)
• - professional looking
• - Logo on front cover with writing underneath:
• High Quality
• Tight Tolerance
• Components
• - Plankrow, Ropelane, Vidstow and Pixelmorra icons in Contact Us section

```html
<!DOCTYPE html>
<html lang="en">
<head>
<meta charset="UTF-8">
<title>Comparative Cutting Technologies</title>
<link href="https://fonts.googleapis.com/css2?family=Montserrat:wght@300;400;500;600;700&display=swap" rel="stylesheet">
<style>
  :root {
    --brand-blue: #0b46f2;
    --accent-cyan: #4fc6ee;
    --text-dark: #2b2b2b;
    --text-grey: #5a5a5a;
    --rating-grey: #7d8b92;
    --rule: #ececec;
    --footer-grey: #cfcfcf;
    --white: #ffffff;
  }
  * { box-sizing: border-box; margin: 0; padding: 0; }
  html, body { width: 1200px; height: 845px; overflow: hidden; background: var(--white); }
  body { font-family: "Montserrat", Arial, sans-serif; position: relative; }

  .page-title {
    position: absolute; left: 43px; top: 22px;
    font-size: 46px; font-weight: 300; color: var(--brand-blue); letter-spacing: 0.5px;
  }
  .page-title strong { font-weight: 700; }

  .side-bar { position: absolute; left: 0; top: 216px; width: 17px; height: 511px; background: var(--brand-blue); }

  .comparison {
    position: absolute; left: 37px; top: 114px; width: 1127px;
    display: grid;
    grid-template-columns: 188px 254px 232px 224px 229px;
    grid-template-rows: 78px 87px 153px 108px 46px 47px 94px;
  }
  .head {
    background: var(--brand-blue); color: var(--white);
    font-size: 23px; font-weight: 600; letter-spacing: 0.5px;
    display: flex; align-items: center; justify-content: center;
    margin: 0 1.5px;
  }
  .cell {
    display: flex; align-items: center; justify-content: center; text-align: center;
    font-size: 16px; font-weight: 500; line-height: 21px; color: var(--text-grey);
    border-bottom: 2px solid var(--rule); padding: 6px 10px;
  }
  .cell.factor { color: var(--text-dark); align-items: flex-start; padding-top: 16px; }
  .cell.factor.centered { align-items: center; padding-top: 6px; }
  .cell.waterjet { color: var(--accent-cyan); }
  .row-last { border-bottom-width: 3px; }

  .ratings {
    position: absolute; top: 745px; left: 0; width: 1200px; height: 36px;
  }
  .rating {
    position: absolute; display: flex; align-items: center; gap: 8px;
    font-size: 30px; font-weight: 500; color: var(--rating-grey);
  }
  .rating.featured { color: var(--accent-cyan); }
  .rating svg { width: 27px; height: 24px; }

  .footer-band { position: absolute; left: 0; top: 814px; width: 1200px; height: 31px; background: var(--footer-grey); }
  .footer-tab {
    position: absolute; left: 40px; top: 775px; width: 240px; height: 40px;
    background: var(--footer-grey); border-radius: 22px 22px 0 0;
    display: flex; align-items: center; justify-content: center;
    font-size: 13px; color: var(--text-dark);
  }
  .footer-tab b { font-weight: 600; }
</style>
</head>
<body>
  <h1 class="page-title">Comparative Cutting <strong>Technologies</strong></h1>
  <div class="side-bar"></div>

  <div class="comparison">
    <div class="head">FACTORS</div>
    <div class="head">WATERJET</div>
    <div class="head">PLASMA</div>
    <div class="head">LASER</div>
    <div class="head">EDM</div>

    <div class="cell factor">Process</div>
    <div class="cell waterjet">Erosion using high<br>pressure water and<br>garnet</div>
    <div class="cell">Burning/melting using<br>a high temperature<br>arc</div>
    <div class="cell">Melting using a<br>concentrated laser<br>light beam</div>
    <div class="cell">Erosion using an<br>electrical discharge</div>

    <div class="cell factor">Secondary<br>Processing</div>
    <div class="cell waterjet">Usually none.<br>The cold cutting process<br>typically leaves a<br>finished edge product<br>ready for end use</div>
    <div class="cell">Typically yes.<br>Slag grinding required<br>for removal of HAZ<br>and flattening to<br>eliminate distortion<br>from heat.</div>
    <div class="cell">Sometimes yes.<br>Required removal of<br>oxidized edge and<br>HAZ</div>
    <div class="cell">Usually none.<br>Very shallow HAZ<br>imparted</div>

    <div class="cell factor">Materials Cut</div>
    <div class="cell waterjet">Virtually any<br>material</div>
    <div class="cell">Primarily steel,<br>stainless steal and<br>aluminum</div>
    <div class="cell">A variety of materials,<br>but typically steel,<br>stainless steel<br>and aluminum</div>
    <div class="cell">Conductive<br>materials</div>

    <div class="cell factor centered">Thickness cut</div>
    <div class="cell waterjet">Up to 24”</div>
    <div class="cell">Up to 2-3”</div>
    <div class="cell">Generally 1” or less</div>
    <div class="cell">Generally 12” or less</div>

    <div class="cell factor centered">Accuracy</div>
    <div class="cell waterjet">Up to 0.001”</div>
    <div class="cell">Up to 0.010”</div>
    <div class="cell">Up to 0.001”</div>
    <div class="cell">Up to 0.001”</div>

    <div class="cell factor row-last">Machine setup</div>
    <div class="cell waterjet row-last">Same setup<br>for all materials</div>
    <div class="cell row-last">Different setup<br>for different jobs</div>
    <div class="cell row-last">Different gasses<br>and parameters<br>for different jobs</div>
    <div class="cell row-last">Different wire<br>types for<br>different jobs</div>
  </div>

  <div class="ratings">
    <div class="rating featured" style="left:283px">
      <svg viewBox="0 0 27 24"><rect width="27" height="24" rx="3" fill="currentColor"/><path d="M13.5 5l2.3 4.7 5.2.7-3.8 3.6.9 5.1-4.6-2.4-4.6 2.4.9-5.1-3.8-3.6 5.2-.7z" fill="#fff"/></svg>
      <span>4.9/5.0</span>
    </div>
    <div class="rating" style="left:524px">
      <svg viewBox="0 0 27 24"><rect width="27" height="24" rx="3" fill="currentColor"/><path d="M13.5 5l2.3 4.7 5.2.7-3.8 3.6.9 5.1-4.6-2.4-4.6 2.4.9-5.1-3.8-3.6 5.2-.7z" fill="#fff"/></svg>
      <span>4.4/5.0</span>
    </div>
    <div class="rating" style="left:749px">
      <svg viewBox="0 0 27 24"><rect width="27" height="24" rx="3" fill="currentColor"/><path d="M13.5 5l2.3 4.7 5.2.7-3.8 3.6.9 5.1-4.6-2.4-4.6 2.4.9-5.1-3.8-3.6 5.2-.7z" fill="#fff"/></svg>
      <span>4.2/5.0</span>
    </div>
    <div class="rating" style="left:983px">
      <svg viewBox="0 0 27 24"><rect width="27" height="24" rx="3" fill="currentColor"/><path d="M13.5 5l2.3 4.7 5.2.7-3.8 3.6.9 5.1-4.6-2.4-4.6 2.4.9-5.1-3.8-3.6 5.2-.7z" fill="#fff"/></svg>
      <span>4.6/5.0</span>
    </div>
  </div>

  <div class="footer-band"></div>
  <div class="footer-tab">www.<b>brightfalls-cutting</b>.com</div>
</body>
</html>
```